KV Taxidermy

I need business Cards with my logo and a background photo of one of my taxidermy mounts.
I would like a black back drop behind it all and what ever looks best for my contact information (red or white?)
Marcus Pellow
555-218-4907
kvtaxidermy512@mailvex.net
Chatterly page

```html
<!DOCTYPE html>
<html lang="en">
<head>
<meta charset="utf-8">
<title>KV Taxidermy – Business Cards</title>
<link rel="stylesheet" href="https://fonts.googleapis.com/css2?family=Archivo:wght@500;700;800&display=swap">
<style>
  :root {
    --ink: #000000;
    --paper: #ffffff;
    --stage: #ffffff;
    --accent: #d0202a;
    --card-edge: #3a3a3a;
    --mount-light: #d9dbd8;
    --mount-mid: #a9aca8;
    --rock: #5c6770;
    --horn: #8a6a45;
  }
  * { box-sizing: border-box; margin: 0; padding: 0; }
  html, body {
    width: 1200px; height: 420px; overflow: hidden;
    background: var(--stage);
    font-family: "Archivo", Arial, sans-serif;
  }
  .sheet {
    position: relative; width: 1200px; height: 420px;
    display: flex; gap: 50px; align-items: center; justify-content: center;
  }
  .card {
    position: relative; width: 560px; height: 320px;
    background: var(--ink); overflow: hidden;
    border: 1px solid var(--card-edge);
  }

  /* ---------- Front ---------- */
  .front__panel {
    position: absolute; left: 0; top: 0; width: 236px; height: 100%;
    background: var(--paper);
  }
  .wordmark {
    display: flex; align-items: center; gap: 8px;
    font-weight: 800; letter-spacing: 0.04em; text-transform: uppercase;
  }
  .wordmark__square { width: 14px; height: 14px; background: currentColor; }
  .front__wordmark {
    position: absolute; left: 0; width: 236px; top: 60px;
    justify-content: center; color: var(--ink); font-size: 17px;
  }
  .mount-photo--resting {
    position: absolute; left: 0; bottom: 0; width: 220px; height: 150px;
    background: linear-gradient(180deg, var(--paper) 0%, var(--mount-light) 35%, var(--mount-mid) 70%, var(--rock) 100%);
  }
  .mount-photo--head {
    position: absolute; right: 0; bottom: 0; width: 132px; height: 155px;
    background: radial-gradient(ellipse at 60% 55%, var(--paper) 0%, var(--mount-light) 45%, var(--horn) 75%, var(--ink) 100%);
  }
  .name-bar {
    position: absolute; left: 236px; top: 85px; width: 264px; height: 29px;
    background: var(--accent); color: var(--paper);
    font-weight: 800; font-size: 20px; letter-spacing: 0.02em;
    display: flex; align-items: center; justify-content: center;
    text-transform: uppercase;
  }
  .contact-list {
    position: absolute; left: 242px; top: 133px;
    list-style: none; display: flex; flex-direction: column; gap: 14px;
    color: var(--paper); font-weight: 700; font-size: 14.5px;
  }
  .contact-list__item { display: flex; align-items: center; gap: 10px; height: 28px; }
  .contact-list__icon { width: 26px; height: 28px; flex: none; }
  .contact-list__square { width: 18px; height: 18px; margin: 0 4px; background: var(--accent); flex: none; }

  /* ---------- Back ---------- */
  .back__wordmark {
    position: absolute; left: 0; right: 0; top: 110px;
    justify-content: center; color: var(--paper); font-size: 24px;
  }
  .back__band { position: absolute; top: 251px; height: 17px; background: var(--accent); }
  .back__band--left { left: 0; width: 191px; }
  .back__band--right { right: 0; width: 196px; }
  .back__phone {
    position: absolute; left: 191px; width: 173px; top: 249px;
    text-align: center; color: var(--paper); font-weight: 700; font-size: 16px;
  }
</style>
</head>
<body>
<main class="sheet">

  <section class="card card--front">
    <div class="front__panel"></div>
    <div class="wordmark front__wordmark"><span class="wordmark__square"></span>KV Taxidermy</div>
    <div class="mount-photo--resting" role="img" aria-label="Photo of a white sheep mount resting on a rock base"></div>
    <div class="mount-photo--head" role="img" aria-label="Photo of a white ram shoulder mount with curled horns"></div>

    <h1 class="name-bar">Marcus Pellow</h1>

    <ul class="contact-list">
      <li class="contact-list__item">
        <svg class="contact-list__icon" viewBox="0 0 26 28" aria-hidden="true">
          <polygon points="13,0 26,7 26,21 13,28 0,21 0,7" fill="var(--accent)"/>
          <rect x="6" y="9" width="14" height="10" fill="var(--paper)"/>
          <polyline points="6,9 13,15 20,9" fill="none" stroke="var(--accent)" stroke-width="1.5"/>
        </svg>
        kvtaxidermy512@mailvex.net
      </li>
      <li class="contact-list__item">
        <svg class="contact-list__icon" viewBox="0 0 26 28" aria-hidden="true">
          <polygon points="13,0 26,7 26,21 13,28 0,21 0,7" fill="var(--accent)"/>
          <path d="M7 10 q6 -4 12 0 l-2 2 h-2 l-1 -1 h-2 l-1 1 h-2 z" fill="var(--paper)"/>
          <rect x="8" y="13" width="10" height="7" rx="1" fill="var(--paper)"/>
        </svg>
        +1 555-218-4907
      </li>
      <li class="contact-list__item">
        <span class="contact-list__square"></span>
        KV Taxidermy
      </li>
    </ul>
  </section>

  <section class="card card--back">
    <div class="wordmark back__wordmark"><span class="wordmark__square"></span>KV Taxidermy</div>
    <div class="back__band back__band--left"></div>
    <p class="back__phone">+1&nbsp;&nbsp;555-218-4907</p>
    <div class="back__band back__band--right"></div>
  </section>

</main>
</body>
</html>
```